Eye Doctor Website

We are looking for a new logo and update to our website.

The Practice Name is Dr. Helen Tarbeck and Associates

This is a simple straight forward project that requires some aspect of Optometry or eye care in the logo. Also we are located in Colorado so if we are open to the idea of adding some element of the Colorado state flag or image of the mountains

For the web all the text is already complete visit www.drhelentarbeck-example.com to see what we currently have we will be taking what you created and updating this site.

We would like the new logo to be used on the web and on business cards.

Please only submit the first page of the web site. Then we can get the rest from there.

Text does not need to be included for the design but would help.

Good luck and let us know if you have any questions

Target Market(s)

30-50 year olds looking for an eye exam.

Site must be fun but also serious and professional to catch the patients attention. Trying to play on outdoor theme

Industry/Entity Type

Flag

Font styles to use
Serif

Colors

Designer to choose colors to be used in the design.

Requirements
Must have
• Need a theme to play off of... Either use the state flag of Colorado or something with mountains. We are very close to the Rocky Mountains so this would work.

Want this them to play throughout the whole site and on Business cards
Nice to have
• Simple navigation. Don't need a lot of text
Should not have
• Clutter.... Simple to the point.

```html
<!DOCTYPE html>
<html lang="en">
<head>
<meta charset="utf-8">
<title>Dr. Helen Tarbeck and Associates</title>
<link href="https://fonts.googleapis.com/css2?family=Libre+Baskerville&family=Source+Sans+3:ital,wght@0,400;0,600;1,400&display=swap" rel="stylesheet">
<style>
:root{
  --blue:#1a9ad8;
  --ink:#333;
  --text:#555;
  --line:#e3e3e3;
  --footer:#3b3c3e;
  --white:#fff;
  --flag-tone:#34509c;
}
*{margin:0;padding:0;box-sizing:border-box}
html,body{width:978px;height:1200px;overflow:hidden;background:var(--white)}
body{position:relative;font-family:"Source Sans 3",Arial,sans-serif;color:var(--text)}
h1,h2,h3,h4{font-weight:400}
.abs{position:absolute}

.brand{left:106px;top:16px;display:flex;align-items:center;gap:12px}
.brand-dot{width:44px;height:44px;border-radius:50%;background:var(--blue)}
.brand-name{font-family:"Libre Baskerville",Georgia,serif;font-size:17px;color:#3d3d3d;letter-spacing:.4px;text-transform:uppercase}
.call{right:109px;top:22px;text-align:right}
.call-label{font-size:11px;color:#555;display:flex;align-items:center;justify-content:flex-end;gap:8px}
.call-number{font-size:14px;color:var(--blue);margin-top:3px}

.nav{left:106px;top:79px;width:766px;height:39px;background:linear-gradient(#f7fbfe,#e7f1fa);display:flex;align-items:center}
.nav a{font-size:10px;color:#444;text-decoration:none;text-transform:uppercase;height:39px;line-height:39px}
.nav .active{background:var(--blue);color:#fff;width:97px;text-align:center}
.nav .item{margin-left:38px}
.nav .item+.item{margin-left:50px}

.hero{left:0;top:118px;width:978px;height:376px;background:linear-gradient(180deg,#b9c8d6 0%,#9aa6a8 35%,#6c7562 60%,#4d5a3c 100%)}
.hero-title{left:297px;top:219px;width:384px;height:37px;background:rgba(70,70,70,.8);color:#fff;font-size:24px;font-weight:600;text-align:center;line-height:37px}
.hero-copy{left:244px;top:279px;width:488px;height:69px;background:rgba(60,60,60,.7);color:#fff;font-size:13px;text-align:center;line-height:24px;padding-top:10px}
.hero-btn{left:362px;top:372px;width:255px;height:40px;background:var(--blue);color:#fff;font-size:12.5px;text-align:center;line-height:40px;text-transform:uppercase}
.dots{left:459px;top:512px;display:flex;gap:6px}
.dots span{width:10px;height:10px;border-radius:50%;background:#d8d8d8}
.dots .on{background:var(--blue)}

.section-title{left:367px;top:568px;width:245px;text-align:center;font-size:21px;color:#444;padding-bottom:8px;border-bottom:1px solid var(--line)}
.service{top:627px;width:179px}
.service-photo{width:179px;height:111px}
.service p{font-size:10.5px;line-height:16px;text-align:center;color:#555;margin-top:17px}
.service.short p{margin-top:19px}
.rule{left:106px;top:836px;width:766px;height:1px;background:var(--line)}

.welcome-title{left:107px;top:876px;font-size:19px;color:#444}
.welcome-title span{color:var(--blue)}
.welcome-copy{left:107px;top:918px;width:440px;font-size:10.5px;line-height:21px;color:#666}
.btn-more{left:108px;top:1039px;width:81px;height:27px;border:1px solid #ccc;font-size:10.5px;color:#444;text-align:center;line-height:25px}

.contact{left:583px;top:880px;width:284px;height:187px;border:1px solid #ddd;display:flex}
.map{width:153px;height:185px;background:linear-gradient(135deg,#e9e6df,#dcd8cf)}
.contact-info{padding:12px 0 0 12px;width:130px}
.contact-info h3{font-size:11px;color:#333}
.contact-info .addr{font-size:9px;line-height:15px;color:#333;margin-top:9px}
.contact-info h4{font-size:11px;color:var(--blue);margin-top:11px}
.contact-info .hours{font-size:9px;line-height:15px;color:#666;margin-top:6px}
.contact-info .more{font-size:9px;font-style:italic;color:#333;text-align:right;margin-top:5px;padding-right:10px}

.footer{left:0;top:1110px;width:978px;height:90px;background:var(--footer)}
.social{left:108px;top:1130px;display:flex;gap:8px}
.social span{width:26px;height:26px;border-radius:50%;border:2px solid #bbb;background:#4a4b4d}
.copyright{left:108px;top:1170px;font-size:10.5px;color:#999}
.flag{left:812px;top:1140px;width:58px;height:35px;border:1px solid #1a1a1a;background:var(--flag-tone)}
</style>
</head>
<body>

<header>
  <div class="abs brand"><span class="brand-dot"></span><span class="brand-name">Dr. Helen Tarbeck and Associates</span></div>
  <div class="abs call">
    <div class="call-label">
      <svg width="11" height="11" viewBox="0 0 12 12"><rect width="12" height="12" rx="2" fill="#ddd"/><path d="M3.5 2.5c-.6.4-.8 1.3-.3 2.5.8 1.8 2.2 3.3 3.9 4 1 .4 1.8.2 2.2-.3l-1.3-1.4-1 .5C6 7.4 5 6.4 4.6 5.4l.6-1z" fill="#fff"/></svg>
      Call Us
    </div>
    <div class="call-number">303.555.0142</div>
  </div>
  <nav class="abs nav">
    <a class="active">Welcome</a>
    <a class="item">Dr. Tarbeck</a>
    <a class="item">Schedule an Appointment</a>
    <a class="item">Office Info/Specials</a>
  </nav>
</header>

<section>
  <div class="abs hero" role="img" aria-label="Rocky Mountain valley with columbine flowers under a cloudy sky"></div>
  <h1 class="abs hero-title">LATEST EYE CARE TECHNOLOGY</h1>
  <p class="abs hero-copy">We are here to provide you and your family with affordable, thorough eye care.<br>Our office employs the latest in eye care technology.</p>
  <div class="abs hero-btn">Schedule an appointment today!</div>
  <div class="abs dots"><span class="on"></span><span></span><span></span><span></span></div>
</section>

<section>
  <h2 class="abs section-title">Our Services</h2>
  <div class="abs service" style="left:106px">
    <div class="service-photo" role="img" aria-label="Patient having an eye exam at a slit lamp" style="background:linear-gradient(135deg,#b6c3cf,#8796a5)"></div>
    <p>Comprehensive eye exams with testing for glaucoma, cataracts, and macular degeneration</p>
  </div>
  <div class="abs service" style="left:302px">
    <div class="service-photo" role="img" aria-label="Person inserting a contact lens" style="background:linear-gradient(135deg,#d9d8d6,#b9a89b)"></div>
    <p>Contact lens exams, including astigmatism (toric), bifocal, and gas permeable lenses</p>
  </div>
  <div class="abs service short" style="left:497px">
    <div class="service-photo" role="img" aria-label="Applying eye drops" style="background:linear-gradient(135deg,#f0ece8,#d2b6a4)"></div>
    <p>Treatment of eye infections, dry eyes, and other eye problems</p>
  </div>
  <div class="abs service short" style="left:693px">
    <div class="service-photo" role="img" aria-label="Child at an eye exam instrument" style="background:linear-gradient(135deg,#6d5a3e,#c4a77c)"></div>
    <p>Pediatric eye exams</p>
  </div>
  <div class="abs rule"></div>
</section>

<section>
  <h2 class="abs welcome-title">Welcome to Our Website <span>Mainpage</span></h2>
  <p class="abs welcome-copy">Welcome to Dr. Helen Tarbeck's optometry office. We are conveniently located in Brightway Market at Larkspur Town Center in Westminster, CO. We are here to provide you and your family with affordable, thorough eye care. Our office employs the latest in eye care technology in order to provide a superior quality of care. We strive to make your visit enjoyable and would be honored to have you as a patient.</p>
  <div class="abs btn-more">Learn More</div>

  <div class="abs contact">
    <div class="map" role="img" aria-label="Street map showing the office location"></div>
    <div class="contact-info">
      <h3>CONTACT US</h3>
      <p class="addr">Dr. Helen Tarbeck and Associates , 2280 Alder Parkway, Westminster</p>
      <h4>Walk-ins Welcome</h4>
      <p class="hours">Monday - 10:00am - 6:00pm, &nbsp;Wednesday 10:00am - 7:00pm</p>
      <p class="more">View More..</p>
    </div>
  </div>
</section>

<footer>
  <div class="abs footer"></div>
  <div class="abs social"><span></span><span></span><span></span><span></span></div>
  <p class="abs copyright">©2014. Yoursite. All right reserved.</p>
  <div class="abs flag" role="img" aria-label="Colorado state flag"></div>
</footer>

</body>
</html>
```